2016 Ledgerline Summit Postcard Design

The Ledgerline Summit. A Summit For Account Chasers...By Account Chasers.
The Ledgerline Summit was created to provide quality content at a reasonable price-point to allow organizations to send multiple attendees and encourage active participation. This event is intended for debt collection professionals who are:

Senior Level Executives
Front Line Collection Managers
Compliance Professionals
Trainers
While there are many great conferences within our industry to choose from, most collection conferences just scratch the surface when attempting to provide real world solutions. The Ledgerline Summit was created to provide debt collection professionals with a foundation of direction, insight, and actionable solutions that can be applied regardless of the size of an organization. Join us at the inaugural Ledgerline Summit as we assemble an expert team of operations, compliance, and training professionals that will deep dive into real world solutions for today’s real world debt collection issues. Here is what you can expect:

Solution driven sessions, not sponsor driven sessions
Substance from "In The Trenches" experts who live it, breathe it, work it...every day
Learn operational, compliance, and training strategies that have proven success
Understand how to efficiently and effectively manage YOUR resources
Apply state of the art technology solutions

Target Market(s)

Debt collection agencies and creditors

Industry/Entity Type

Financial Service

Font styles to use
Serif

Requirements
Must have
• link to website www.LLS2016.example and use of image provided LLSCover. Use same color scheme as the LLSCover image

```html
<!DOCTYPE html>
<html lang="en">
<head>
<meta charset="utf-8">
<title>2016 Ledgerline Summit Postcard</title>
<link href="https://fonts.googleapis.com/css2?family=Oswald:wght@200;300;500;700&family=Open+Sans:wght@300;400;700&family=Dancing+Script:wght@500&display=swap" rel="stylesheet">
<style>
:root{
  --lime:#d6e15c;
  --teal:#1a9597;
  --teal-bright:#1ea3a8;
  --sky:#35b8c9;
  --ink:#1b1b1b;
  --paper:#ffffff;
  --stamp:#b8b9bb;
  --stage:#e9e6e1;
}
*{box-sizing:border-box;margin:0;padding:0}
html,body{width:874px;height:1200px;overflow:hidden;background:var(--stage)}
.canvas{position:relative;width:874px;height:1200px}
.card{position:absolute;left:74px;width:726px;overflow:hidden;box-shadow:0 4px 10px rgba(0,0,0,.25)}
.card--front{top:74px;height:517px}
.card--back{top:626px;height:516px;background:var(--paper)}

/* front */
.hero-photo{position:absolute;inset:0;background:linear-gradient(180deg,#8a8a8a 0%,#5e5e5e 30%,#3a3a3a 55%,#1e1e1e 100%)}
.headline{position:absolute;left:21px;top:12px;font:700 30px/46px 'Oswald',sans-serif;color:var(--lime);text-shadow:1px 1px 2px rgba(0,0,0,.6)}
.date-label{position:absolute;left:24px;top:130px;font:500 20px 'Dancing Script',cursive;color:var(--lime)}
.dates{position:absolute;left:21px;top:162px;font:700 18px/27px 'Oswald',sans-serif;color:var(--lime);text-shadow:1px 1px 2px rgba(0,0,0,.6)}
.intro{position:absolute;left:21px;top:229px;width:232px;font:400 10.5px/17.4px 'Open Sans',sans-serif;color:#fff;text-align:justify}
.audience{position:absolute;left:21px;top:347px;list-style:none}
.audience li{font:700 13.5px/23px 'Open Sans',sans-serif;color:#fff;display:flex;align-items:center}
.dot{display:inline-block;width:12px;height:12px;border-radius:50%;background:radial-gradient(circle at 35% 35%,#e8f07a,#8ea61c);margin-right:8px;flex:none}
.location{position:absolute;left:380px;top:162px;width:346px;height:47px;background:var(--teal-bright);color:#fff;padding:5px 26px 0 6px;text-align:right;font:500 13.5px/18px 'Oswald',sans-serif}
.location em{font:500 15px 'Dancing Script',cursive;font-style:normal;float:left}
.title-panel{position:absolute;left:380px;top:209px;width:346px;height:217px;background:rgba(20,20,20,.55);border-left:1px solid rgba(255,255,255,.35)}
.title-name{position:absolute;left:26px;top:22px;font:200 44px/66px 'Oswald',sans-serif;color:#fff;letter-spacing:6px}
.title-name .year{color:var(--sky);font-weight:300}
.title-tag{position:absolute;left:26px;top:190px;font:400 12px 'Open Sans',sans-serif;color:#ddd}
.rule{position:absolute;left:405px;top:426px;width:288px;height:1px;background:#888}
.meta{position:absolute;left:172px;top:437px;font:700 16px 'Open Sans',sans-serif;color:#fff;letter-spacing:.3px}
.meta .sep{margin:0 8px;font-weight:400}
.contact-bar{position:absolute;left:0;top:473px;width:726px;height:44px}
.contact-bar svg{position:absolute;inset:0}
.contact-phone{position:absolute;left:26px;top:3px;font:700 23px 'Oswald',sans-serif;color:#fff}
.contact-web{position:absolute;right:30px;top:3px;font:700 23px 'Oswald',sans-serif;color:#fff}

/* back */
.story{position:absolute;left:19px;top:22px;width:528px;font:400 11.5px/17.4px 'Open Sans',sans-serif;color:var(--ink);text-align:justify}
.stamp{position:absolute;left:598px;top:25px;width:101px;height:105px;background:var(--stamp)}
.expect{position:absolute;left:18px;top:152px;width:370px;height:340px;background:var(--teal)}
.expect h2{position:absolute;left:19px;top:5px;font:300 21px 'Open Sans',sans-serif;color:#fff}
.expect ul{position:absolute;left:20px;top:48px;width:340px;list-style:none}
.expect li{display:flex;font:400 12.5px/17px 'Open Sans',sans-serif;color:#fff;margin-bottom:6px}
.expect li .dot{margin-top:3px;width:11px;height:11px}
.event-photo{position:absolute;top:223px;height:108px}
.event-photo--room{left:10px;width:193px;background:linear-gradient(180deg,#c9c2b4,#6e6b75 60%,#8b4a5e)}
.event-photo--hall{left:212px;width:149px;background:linear-gradient(180deg,#c8a65a,#6d4a3a 50%,#3f6b5a 80%,#a5322f)}
.address-line{position:absolute;left:416px;width:283px;height:1px;background:#777}
.back-web{position:absolute;left:403px;top:440px;width:299px;text-align:center;font:700 33px 'Oswald',sans-serif;color:var(--teal);letter-spacing:1.5px;border-bottom:1px solid #555;padding-bottom:2px}
</style>
</head>
<body>
<div class="canvas">

  <section class="card card--front">
    <div class="hero-photo" role="img" aria-label="Black and white photo of a city skyline and river with a rocky shoreline"></div>
    <h1 class="headline">The Ledgerline Summit. A Summit For<br>Account Chasers... By Account Chasers</h1>
    <div class="date-label">Date:</div>
    <p class="dates">March 21 - Monday, 2016<br>March 23 - Wednesday, 2016</p>
    <p class="intro">The Ledgerline Summit was created to provide quality content at a reasonable price-point to allow organizations to send multiple attendees and encourage active participation. This event is intended for debt collection professionals who are:</p>
    <ul class="audience">
      <li><span class="dot"></span>Senior Level Executives</li>
      <li><span class="dot"></span>Front Line Collection Managers</li>
      <li><span class="dot"></span>Compliance Professionals</li>
      <li><span class="dot"></span>Trainers</li>
    </ul>
    <div class="location"><em>Location:</em>Harborline Event Center, 100 Harborline Way<br>Saint Charles, Missouri 63301 USA</div>
    <div class="title-panel">
      <div class="title-name">LEDGERLINE<br>SUMMIT <span class="year">2016</span></div>
      <div class="title-tag">A Summit for account chasers... by account chasers.</div>
    </div>
    <div class="rule"></div>
    <div class="meta">SAINT LOUIS, MISSOURI<span class="sep">|</span>MARCH 21, 2016 - MARCH 23, 2016</div>
    <div class="contact-bar">
      <svg width="726" height="44" viewBox="0 0 726 44" aria-hidden="true">
        <rect width="726" height="44" fill="var(--sky)"/>
        <polygon points="0,0 362,0 394,44 0,44" fill="var(--lime)"/>
      </svg>
      <div class="contact-phone">Contact us: (555) 014-2016</div>
      <div class="contact-web">www.LLS2016.example</div>
    </div>
  </section>

  <section class="card card--back">
    <p class="story">While there are many great conferences within our industry to choose from, most collection conferences just scratch the surface when attempting to provide real world solutions. The Ledgerline Summit was created to provide debt collection professionals with a foundation of direction, insight, and actionable solutions that can be applied regardless of the size of an organization. Join us at the inaugural Ledgerline Summit as we assemble an expert team of operations, compliance, and training professionals that will deep dive into real world solutions for today’s real world debt collection issues.</p>
    <div class="stamp"></div>
    <div class="expect">
      <h2>Here is what you can expect:</h2>
      <ul>
        <li><span class="dot"></span><span>Solution driven sessions, not sponsor driven sessions</span></li>
        <li><span class="dot"></span><span>Substance from "In The Trenches" experts who live<br>it, breathe it, work it...every day</span></li>
        <li><span class="dot"></span><span>Learn operational, compliance, and training<br>strategies that have proven success</span></li>
        <li><span class="dot"></span><span>Understand how to efficiently and effectively<br>manage YOUR resources</span></li>
        <li><span class="dot"></span><span>Apply state of the art technology solutions</span></li>
      </ul>
      <div class="event-photo event-photo--room" role="img" aria-label="Photo of a conference room filled with seated attendees"></div>
      <div class="event-photo event-photo--hall" role="img" aria-label="Photo of the venue's gaming hall with an ornate ceiling"></div>
    </div>
    <div class="address-line" style="top:293px"></div>
    <div class="address-line" style="top:331px"></div>
    <div class="address-line" style="top:369px"></div>
    <div class="address-line" style="top:406px"></div>
    <div class="back-web">www.LLS2016.example</div>
  </section>

</div>
</body>
</html>
```